CloudForge Business Card

I need something that flows with the logo and looks professional but creative. I included the thumbnail file of the photo but will upload the source file once I have it. Colors of business card should flow. I am interested in doing the translucent clear plastic cards as well. My company is called CloudForge in one word and the contact details are below:

Dean Holloway
832-574-2938
www.CloudForgeTx.example
dholloway_47@mailbox.example
Updates

Too much red. I'd rather focus on the blue and put some silver or grey in there.

New Files uploaded. Like the designs so far and am looking forward to seeing more.

Looking for a whole new direction. Let's forget about the plastic card. Let's focus on the blue more than red. I still haven't seen something that really grabs me.

Industry/Entity Type

Plastic

```html
<!DOCTYPE html>
<html lang="en">
<head>
<meta charset="UTF-8">
<title>CloudForge Business Card</title>
<link rel="stylesheet" href="https://fonts.googleapis.com/css2?family=Alegreya+Sans+SC:wght@400;800&display=swap">
<style>
  :root {
    --backdrop: #e8e3da;
    --card: #262829;
    --card-edge: #1c1d1e;
    --accent-blue: #2fa3dc;
    --contact-blue: #3ba7d9;
    --glow-blue: rgba(43, 143, 196, 0.38);
    --glow-fade: rgba(43, 143, 196, 0);
  }
  * { margin: 0; padding: 0; box-sizing: border-box; }
  html, body {
    width: 1200px;
    height: 1000px;
    overflow: hidden;
    background: var(--backdrop);
    font-family: "Alegreya Sans SC", sans-serif;
  }
  .sheet {
    position: relative;
    width: 1200px;
    height: 1000px;
  }
  .card {
    position: absolute;
    left: 250px;
    width: 700px;
    height: 400px;
    background: linear-gradient(160deg, #2e3031 0%, var(--card) 55%, var(--card-edge) 100%);
    border-radius: 6px;
    box-shadow: 0 10px 28px rgba(0,0,0,0.25);
    overflow: hidden;
  }
  .card--front { top: 60px; }
  .card--back { top: 540px; }

  .card__ornament {
    position: absolute;
    left: 0;
    bottom: 0;
    width: 380px;
    height: 170px;
    background: radial-gradient(ellipse 100% 100% at 0% 100%, var(--glow-blue) 0%, var(--glow-fade) 70%);
  }
  .brand-name {
    position: absolute;
    font-weight: 800;
    color: var(--accent-blue);
    letter-spacing: 1px;
    line-height: 1;
    white-space: nowrap;
  }
  .card--front .brand-name {
    right: 90px;
    top: 150px;
    font-size: 92px;
  }
  .card--back .brand-name {
    right: 44px;
    bottom: 40px;
    font-size: 40px;
  }
  .contact {
    position: absolute;
    left: 50px;
    top: 46px;
    list-style: none;
    color: var(--contact-blue);
    font-size: 27px;
    font-weight: 400;
    line-height: 1.45;
    letter-spacing: 0.5px;
  }
</style>
</head>
<body>
<main class="sheet">
  <section class="card card--front" aria-label="Card front">
    <div class="card__ornament" role="img" aria-label="Flowing blue light-line ornament"></div>
    <div class="brand-name">CloudForge</div>
  </section>

  <section class="card card--back" aria-label="Card back">
    <ul class="contact">
      <li class="contact__name">Dean Holloway</li>
      <li class="contact__phone">832-574-2938</li>
      <li class="contact__web">www.CloudForgeTx.example</li>
      <li class="contact__email">dholloway_47@mailbox.example</li>
    </ul>
    <div class="brand-name">CloudForge</div>
  </section>
</main>
</body>
</html>
```